business card with logo

Would like a business card for an electrical contractor called BRANNOCK ELECTRICS.
No generic electrical imagery (light globe, powerpoints, ect). Would like a logo or symbol created in the design as part of the project . I would like crisp colour. No templated designs like Dorvex

is there any other designers willing to submit designs

Electrical

```html
<!DOCTYPE html>
<html lang="en">
<head>
<meta charset="utf-8">
<title>Brannock Electrics – Business Card</title>
<link rel="stylesheet" href="https://fonts.googleapis.com/css2?family=Open+Sans:wght@400;600;700&display=swap">
<style>
  :root {
    --page: #e9ebee;
    --card-black: #0b0d10;
    --card-black-soft: #1b1f25;
    --navy-deep: #0b1a33;
    --navy-mid: #16305a;
    --cyan: #1fa6e0;
    --cyan-light: #3cc0f2;
    --text-light: #e8eef4;
    --text-muted: #b9c6d3;
  }
  * { box-sizing: border-box; margin: 0; padding: 0; }
  html, body {
    width: 1200px;
    height: 1023px;
    overflow: hidden;
    background: var(--page);
    font-family: "Open Sans", Arial, sans-serif;
  }
  .sheet {
    width: 1200px;
    height: 1023px;
    display: flex;
    flex-direction: column;
    align-items: center;
    justify-content: center;
    gap: 60px;
  }
  .card {
    position: relative;
    width: 700px;
    height: 400px;
    border-radius: 22px;
    overflow: hidden;
    box-shadow: 0 10px 30px rgba(0, 0, 0, 0.25);
  }

  /* Front */
  .front__top {
    position: absolute;
    inset: 0 0 auto 0;
    height: 188px;
    background: linear-gradient(180deg, var(--card-black-soft), var(--card-black));
  }
  .brand {
    position: absolute;
    left: 56px;
    top: 64px;
    display: flex;
    align-items: center;
    gap: 16px;
  }
  .brand__mark {
    width: 22px;
    height: 22px;
    background: var(--cyan);
  }
  .brand__name {
    font-weight: 600;
    font-size: 44px;
    letter-spacing: 2px;
    color: var(--cyan);
    line-height: 1;
  }
  .band {
    position: absolute;
    left: 0;
    right: 0;
    height: 22px;
    background: var(--cyan);
    display: flex;
    align-items: center;
    justify-content: flex-end;
    padding-right: 22px;
  }
  .front .band { top: 188px; }
  .band__licence {
    font-size: 13px;
    color: var(--navy-deep);
    letter-spacing: 0.5px;
  }
  .front__bottom {
    position: absolute;
    inset: 210px 0 0 0;
    background: linear-gradient(160deg, var(--navy-mid), var(--navy-deep));
  }
  .person {
    position: absolute;
    left: 56px;
    bottom: 44px;
  }
  .person__name {
    font-weight: 700;
    font-size: 22px;
    color: var(--cyan);
    letter-spacing: 0.5px;
  }
  .person__role {
    font-size: 15px;
    color: var(--text-light);
    margin-top: 2px;
  }
  .contacts {
    position: absolute;
    right: 40px;
    top: 236px;
    list-style: none;
    display: flex;
    flex-direction: column;
    gap: 8px;
  }
  .contacts__item {
    display: flex;
    align-items: center;
    gap: 10px;
    font-size: 16px;
    color: var(--text-light);
  }
  .contacts__icon {
    width: 16px;
    height: 16px;
    flex: none;
  }

  /* Back */
  .back {
    background: linear-gradient(180deg, var(--card-black-soft), var(--card-black));
  }
  .back .brand {
    left: 50%;
    top: 150px;
    transform: translateX(-50%);
  }
  .back .band { top: 300px; }
  .back__foot {
    position: absolute;
    inset: 322px 0 0 0;
    background: linear-gradient(160deg, var(--navy-mid), var(--navy-deep));
  }
</style>
</head>
<body>
<main class="sheet">

  <section class="card front" aria-label="Business card front">
    <div class="front__top"></div>
    <div class="brand">
      <span class="brand__mark"></span>
      <span class="brand__name">BRANNOCK ELECTRICS</span>
    </div>
    <div class="band"><span class="band__licence">rec#20485</span></div>
    <div class="front__bottom" role="img" aria-label="Dark blue carbon-fibre texture"></div>

    <div class="person">
      <p class="person__name">LIAM BRANNOCK</p>
      <p class="person__role">Director</p>
    </div>

    <ul class="contacts">
      <li class="contacts__item">
        <svg class="contacts__icon" viewBox="0 0 16 16" aria-hidden="true">
          <rect width="16" height="16" rx="2" fill="#1fa6e0"/>
          <path d="M5 3.5h2l1 3-1.3 1a6 6 0 0 0 2.8 2.8l1-1.3 3 1v2A1 1 0 0 1 12.5 13 9.5 9.5 0 0 1 3 3.5 1 1 0 0 1 4 2.5z" fill="#0b1a33" transform="translate(-0.5 0.5) scale(0.95)"/>
        </svg>
        0140 222 318
      </li>
      <li class="contacts__item">
        <svg class="contacts__icon" viewBox="0 0 16 16" aria-hidden="true">
          <rect width="16" height="16" rx="2" fill="#1fa6e0"/>
          <rect x="5" y="2.5" width="6" height="11" rx="1.2" fill="#0b1a33"/>
          <rect x="6" y="4" width="4" height="7" fill="#1fa6e0"/>
        </svg>
        0961 735 204
      </li>
      <li class="contacts__item">
        <svg class="contacts__icon" viewBox="0 0 16 16" aria-hidden="true">
          <rect width="16" height="16" rx="2" fill="#1fa6e0"/>
          <rect x="3" y="4.5" width="10" height="7" fill="#0b1a33"/>
          <path d="M3 4.5l5 4 5-4" fill="none" stroke="#1fa6e0" stroke-width="1.2"/>
        </svg>
        brannockelec@mailnest.net
      </li>
    </ul>
  </section>

  <section class="card back" aria-label="Business card back">
    <div class="brand">
      <span class="brand__mark"></span>
      <span class="brand__name">BRANNOCK ELECTRICS</span>
    </div>
    <div class="band"><span class="band__licence">rec#20485</span></div>
    <div class="back__foot" role="img" aria-label="Dark blue carbon-fibre texture"></div>
  </section>

</main>
</body>
</html>
```